Business Card Design- Mortgage Firm

Looking to design a business Card for our Outside sales people. This card is used to provide their contact information to prospective clients and realtors. Must have All Pertinent company and licensing information by law. We are looking for a very modern design that flows with our current logo color scheme. Red/White/Black

Industry/Entity Type

Mortgage Lender

Contact Information for Business Card

Must stick with current color scheme.

Colors
f04a50
ffffff
ecf7fb

Requirements
Must have
• Company Logo or similar
• Company Address (748 W Alder Avenue, Suite 312, Corona CA 92879 NMLS: 4072916)
• Agent Name (Mira Talbot)
• Title (Senior Mortgage Loan Originator)
• NMLS# 8395021
• Toll Free: 800-627-3184
• Direct : 310-555-4860
Nice to have
• Room for Agent Picture

```html
<!DOCTYPE html>
<html lang="en">
<head>
<meta charset="UTF-8">
<title>Vantage Home Lending – Business Card</title>
<link rel="stylesheet" href="https://fonts.googleapis.com/css2?family=Lato:wght@400;700&display=swap">
<style>
  :root {
    --brand-red: #b41e25;
    --card-white: #ffffff;
    --stage: #ecedef;
    --portrait-grey: #8a8a8a;
    --ink-light: #ffffff;
  }
  * { margin: 0; padding: 0; box-sizing: border-box; }
  html, body {
    width: 1200px;
    height: 900px;
    overflow: hidden;
    background: var(--stage);
    font-family: "Lato", sans-serif;
  }
  .canvas { position: relative; width: 1200px; height: 900px; }

  .card {
    position: absolute;
    overflow: hidden;
    box-shadow: 0 6px 18px rgba(0,0,0,0.18);
  }

  /* Front */
  .card-front {
    left: 178px; top: 74px;
    width: 588px; height: 364px;
    background: var(--card-white);
  }
  .front-band {
    position: absolute;
    left: 0; top: 170px;
    width: 100%; height: 194px;
    background: var(--brand-red);
  }
  .agent-portrait {
    position: absolute;
    left: 0; top: 26px;
    width: 328px; height: 338px;
    background: var(--portrait-grey);
    border-radius: 120px 120px 0 0;
  }
  .brand-lockup {
    position: absolute;
    right: 38px; top: 56px;
    display: flex;
    align-items: center;
    gap: 12px;
  }
  .brand-mark {
    width: 40px; height: 40px;
    background: var(--brand-red);
  }
  .brand-name {
    color: var(--brand-red);
    font-weight: 700;
    font-size: 27px;
    line-height: 1.15;
    letter-spacing: 1px;
    text-align: left;
  }
  .agent-details {
    position: absolute;
    right: 38px; top: 196px;
    text-align: right;
    color: var(--ink-light);
  }
  .agent-name {
    font-weight: 700;
    font-size: 21px;
    line-height: 26px;
  }
  .agent-title {
    font-size: 17px;
    line-height: 22px;
    margin-bottom: 8px;
  }
  .agent-phones, .agent-address {
    font-size: 16.5px;
    line-height: 21px;
  }
  .agent-phones { margin-bottom: 6px; }

  /* Back */
  .card-back {
    left: 388px; top: 506px;
    width: 566px; height: 350px;
    background: var(--brand-red);
  }
  .back-lockup {
    position: absolute;
    left: 0; top: 118px;
    width: 100%;
    display: flex;
    justify-content: center;
    align-items: center;
    gap: 16px;
  }
  .back-mark {
    width: 54px; height: 54px;
    background: var(--card-white);
  }
  .back-name {
    color: var(--card-white);
    font-weight: 700;
    font-size: 34px;
    line-height: 1.15;
    letter-spacing: 1px;
  }
  .licensing {
    position: absolute;
    left: 0; top: 292px;
    width: 100%;
    text-align: center;
    color: var(--ink-light);
    font-size: 15.5px;
    word-spacing: 2px;
  }
</style>
</head>
<body>
<main class="canvas">

  <section class="card card-front">
    <div class="front-band"></div>
    <div class="agent-portrait" role="img" aria-label="Agent headshot photo"></div>

    <div class="brand-lockup">
      <span class="brand-mark"></span>
      <span class="brand-name">VANTAGE<br>HOME LENDING</span>
    </div>

    <div class="agent-details">
      <p class="agent-name">MIRA TALBOT</p>
      <p class="agent-title">Senior Mortgage Loan Originator</p>
      <p class="agent-phones">Toll Free: 800-627-3184<br>Direct : 310-555-4860</p>
      <p class="agent-address">748 W Alder Avenue, Suite 312<br>Corona CA 92879</p>
    </div>
  </section>

  <section class="card card-back">
    <div class="back-lockup">
      <span class="back-mark"></span>
      <span class="back-name">VANTAGE<br>HOME LENDING</span>
    </div>
    <p class="licensing">NMLS: 4072916 &nbsp;&nbsp;| NMLS# 8395021</p>
  </section>

</main>
</body>
</html>
```